Kestrelwood Restaurnt Lunch Menu Redesign:

We have two lunch special menus that need to be reformatted into a 4.25inx11in and need a graphics design update. Some menu items need to change and some descriptions need to updated. This new menu should double sided with the Main Dining Lunch Menu on the front side and Teppanyaki Lunch menu on the back.

Both menus should follow the same design formatting as the main dining lunch menu (font, sizing, ect.)

```html
<!DOCTYPE html>
<html lang="en">
<head>
<meta charset="utf-8">
<title>Kestrelwood Restaurnt – Lunch Menu</title>
<link href="https://fonts.googleapis.com/css2?family=Ubuntu:wght@500;700&family=Open+Sans:ital,wght@0,400;0,600;1,400&display=swap" rel="stylesheet">
<style>
  :root {
    --slate: #556867;
    --slate-dark: #4d605f;
    --gold: #c8b685;
    --gold-text: #c2ad72;
    --panel: #f4f5f7;
    --stripe: #e9e9ec;
    --ink: #1f1f1f;
    --ink-soft: #333;
    --page: #ffffff;
  }
  * { box-sizing: border-box; margin: 0; padding: 0; }
  html, body { width: 932px; height: 1200px; overflow: hidden; background: var(--page); }
  body { position: relative; font-family: "Open Sans", sans-serif; color: var(--ink); }

  .menu-side {
    position: absolute; top: 129px; width: 399px; height: 1033px;
    background: var(--panel); overflow: hidden;
  }
  .menu-side--front { left: 45px; }
  .menu-side--back { left: 486px; }
  .menu-side > * { position: absolute; }

  .brand-badge {
    background: var(--slate); border-radius: 4px; color: #fff;
    display: flex; flex-direction: column; align-items: center; justify-content: center;
    font-family: "Ubuntu", sans-serif; font-weight: 700; line-height: 1.1; text-align: center;
  }
  .brand-badge--front { left: 139px; top: 21px; width: 122px; height: 52px; font-size: 13px; }
  .brand-badge--back { left: 129px; top: 22px; width: 140px; height: 59px; font-size: 15px; }

  .menu-title {
    left: 0; width: 100%; top: 86px; text-align: center;
    font-family: "Ubuntu", sans-serif; font-weight: 700; font-size: 26px; color: var(--slate);
  }
  .hours-pill {
    left: 119px; top: 122px; width: 160px; height: 23px; border-radius: 4px;
    background: var(--gold); color: #fff; font-size: 13px;
    display: flex; align-items: center; justify-content: center;
  }

  .section-heading {
    font-family: "Ubuntu", sans-serif; font-weight: 700; font-size: 18px; color: var(--slate);
    border-top: 1px solid var(--gold); border-bottom: 1px solid var(--gold);
    height: 27px; line-height: 25px; white-space: nowrap;
  }
  .section-note {
    border-left: 1px solid var(--slate); padding-left: 6px;
    font-size: 6.6px; line-height: 1.3; color: var(--ink-soft);
  }
  .section-note strong { font-weight: 600; color: var(--slate); }
  .section-note .price-accent { color: var(--gold-text); font-weight: 600; font-size: 7.5px; }

  .item-list { display: flex; flex-direction: column; }
  .item {
    display: flex; justify-content: space-between; align-items: center;
    padding: 0 6px 0 2px; height: 26px;
  }
  .item--tall { height: 35px; }
  .item:nth-child(even) { background: var(--stripe); }
  .item-name { font-size: 12px; line-height: 1.15; }
  .item-name em { font-size: 9.5px; color: var(--ink-soft); }
  .item-desc { display: block; font-style: italic; font-size: 9.5px; color: var(--ink-soft); }
  .item-price { font-size: 11.5px; color: #555; white-space: nowrap; }

  .sandwich-list .item { height: 37px; }

  .sushi-list .item { height: 21px; margin-bottom: 5px; padding-left: 2px; }
  .sushi-list .item-name em { font-size: 9.5px; }
  .sushi-list--plain .item:nth-child(even) { background: transparent; }
  .sushi-list--ruled { border-left: 1.5px solid var(--gold); padding-left: 6px; }
  .sushi-list--ruled .item:nth-child(even) { background: transparent; }

  .food-photo { width: 78px; height: 80px; }
  .photo-warm { background: linear-gradient(160deg, #c9a67a, #6f5a3d 55%, #3f4a2c); }
  .photo-dark { background: linear-gradient(170deg, #3b2c25, #a36a3a 50%, #2a2a24); }
  .photo-plate { background: linear-gradient(150deg, #d6d2cc, #7a5b3c 55%, #c9c3ba); }
  .photo-gold { background: linear-gradient(150deg, #e7e3dd, #d6a640 50%, #efece8); }
  .photo-rice { background: linear-gradient(160deg, #4a3a2e, #c8a36a 55%, #e3ddd2); }
  .photo-sushi { background: linear-gradient(165deg, #c96a3a, #e8d9c4 50%, #3c3c3e); }
  .photo-sashimi { background: linear-gradient(160deg, #7b7d78, #d8bca8 50%, #e9e4df); }

  .scenery-fade {
    left: 0; top: 802px; width: 100%; height: 179px;
    background: linear-gradient(180deg, rgba(220,222,225,0) 0%, rgba(220,222,225,0.55) 100%);
  }

  .footer-band {
    left: 0; top: 981px; width: 100%; height: 52px; background: var(--slate-dark);
    color: #fff; display: flex; align-items: center;
  }
  .footer-band--front { flex-direction: column; justify-content: center; font-style: italic; font-size: 9.6px; line-height: 1.3; text-align: center; }
  .footer-band--front .accent { color: var(--gold); font-weight: 600; font-style: normal; }
  .footer-band--back { gap: 11px; padding-left: 63px; font-size: 9.5px; }
  .footer-band svg.curve { position: absolute; top: -6px; left: 0; }
  .social-label { border-bottom: 1px solid #fff; padding-bottom: 2px; }
  .social-dots { display: flex; gap: 6px; margin-left: 0; }
  .social-dot { width: 21px; height: 21px; border-radius: 5px; background: #fff; }
  .social-handle { letter-spacing: 2.2px; border-bottom: 1px solid #fff; padding-bottom: 2px; margin-left: 2px; }

  .rule-gold { left: 39px; top: 764px; width: 319px; height: 1.5px; background: var(--gold); }
</style>
</head>
<body>

<!-- Front: Main dining lunch -->
<section class="menu-side menu-side--front">
  <div class="brand-badge brand-badge--front"><span>Kestrelwood</span><span>Restaurnt</span></div>
  <h1 class="menu-title">Lunch Specials</h1>
  <div class="hours-pill">Served Daily 11AM - 3PM</div>

  <h2 class="section-heading" style="left:38px; top:172px;">Sandwiches</h2>
  <p class="section-note" style="left:148px; top:171px; height:28px; padding-top:4px;">Served with Choice of Miso Soup<br>or House Salad &amp; Potato Chips</p>
  <div class="item-list sandwich-list" style="left:38px; top:211px; width:225px;">
    <div class="item"><span class="item-name">Fried Breaded Calamari Steak<span class="item-desc">with Tomato, Lettuce &amp; Onion</span></span><span class="item-price">$ 16</span></div>
    <div class="item"><span class="item-name">Grilled Chicken <em>with Bacon, Tomato,</em><span class="item-desc">Lettuce &amp; Mayonnaise Drizzle</span></span><span class="item-price">$ 16</span></div>
    <div class="item"><span class="item-name">Hamburger <em>with Lettuce, Tomato,</em><span class="item-desc">Onion, Mayonnaise Drizzle</span></span><span class="item-price">$ 18</span></div>
    <div class="item"><span class="item-name">Fried Soft Shell Crab Burger<span class="item-desc">with Avocado, Lettuce, Tomato, Onion &amp; Mayo</span></span><span class="item-price">$ 20</span></div>
  </div>
  <div class="food-photo photo-warm" style="left:280px; top:173px;" role="img" aria-label="Photo of a calamari steak sandwich with salad"></div>
  <div class="food-photo photo-dark" style="left:280px; top:262px;" role="img" aria-label="Photo of a hamburger with fries"></div>

  <h2 class="section-heading" style="left:38px; top:391px;">Sushi Specials</h2>
  <p class="section-note" style="left:206px; top:391px;"><strong>Please Select 4 of the followings for </strong><span class="price-accent">$16</span><br>Served with a 4 piece California Roll &amp;<br>Miso Soup or House Salad</p>
  <div class="item-list sushi-list" style="left:38px; top:432px; width:138px;">
    <div class="item"><span class="item-name">Hamachi <em>Yellowtail Tuna</em></span></div>
    <div class="item"><span class="item-name">Hotate <em>Yellowtail</em></span></div>
    <div class="item"><span class="item-name">Ika <em>Squid</em></span></div>
    <div class="item"><span class="item-name">Ikura <em>Salmon Roe</em></span></div>
    <div class="item"><span class="item-name">Saba <em>Mackerel</em></span></div>
    <div class="item"><span class="item-name">Sake <em>Salmon</em></span></div>
    <div class="item"><span class="item-name">Tai <em>Red Snapper</em></span></div>
  </div>
  <div class="item-list sushi-list" style="left:206px; top:432px; width:138px;">
    <div class="item"><span class="item-name">Maguro <em>Yellowtail Tuna</em></span></div>
    <div class="item"><span class="item-name">Smoked Salmon</span></div>
  </div>
  <div class="item-list sushi-list sushi-list--ruled" style="left:206px; top:506px; width:138px;">
    <div class="item"><span class="item-name">Tako <em>Octopus</em></span></div>
    <div class="item"><span class="item-name">Unagi <em>BBQ Eel</em></span></div>
    <div class="item"><span class="item-name">Ebi <em>Shrimp</em></span></div>
    <div class="item"><span class="item-name">Tamago <em>Egg</em></span></div>
  </div>

  <h2 class="section-heading" style="left:38px; top:647px; width:152px;">Main Courses</h2>
  <p class="section-note" style="left:206px; top:647px;"><strong>Served with Rice &amp; Choice of<br>Miso Soup or House Salad</strong><br>All Meals Served with Rice.<br>Upgrade to fried rice for only $4</p>
  <div class="item-list" style="left:38px; top:687px; width:225px;">
    <div class="item item--tall"><span class="item-name">Organic Tofu Teriyaki<span class="item-desc">Served Grilled or Tempura Fried</span></span><span class="item-price">$ 14</span></div>
    <div class="item"><span class="item-name">Chicken Teriyaki</span><span class="item-price">$ 16</span></div>
    <div class="item"><span class="item-name">Spicy Chicken Teriyaki</span><span class="item-price">$ 16</span></div>
    <div class="item"><span class="item-name">Beef Teriyaki</span><span class="item-price">$ 16</span></div>
    <div class="item"><span class="item-name">Spicy Beef Teriyaki</span><span class="item-price">$ 16</span></div>
    <div class="item item--tall"><span class="item-name">Chicken Kats<span class="item-desc">Breaded Chicken Breast</span></span><span class="item-price">$ 15</span></div>
    <div class="item item--tall"><span class="item-name">Katsu Don<span class="item-desc">Fried Chicken Breast, Egg &amp; Onion over Rice</span></span><span class="item-price">$ 16</span></div>
    <div class="item item--tall"><span class="item-name">Unagi Don<span class="item-desc">BBQ Eel over Rice</span></span><span class="item-price">$ 19</span></div>
    <div class="item"><span class="item-name">Shrimp &amp; Vegetable Tempura</span><span class="item-price">$ 16</span></div>
  </div>
  <div class="food-photo photo-plate" style="left:280px; top:692px;" role="img" aria-label="Photo of teriyaki with tempura and rice"></div>
  <div class="food-photo photo-sushi" style="left:280px; top:781px;" role="img" aria-label="Photo of a sushi roll platter"></div>
  <div class="food-photo photo-sashimi" style="left:280px; top:870px;" role="img" aria-label="Photo of a sashimi plate"></div>

  <footer class="footer-band footer-band--front">
    <svg class="curve" width="399" height="8" viewBox="0 0 399 8" aria-hidden="true"><path d="M0 6 Q200 -2 399 0 L399 8 L0 8 Z" fill="#4d605f"/></svg>
    <p><span class="accent">Served Raw:</span> 20% gratuity added to parties of 6 or more.</p>
    <p>Consuming raw or undercooked food may increase your risk of foodborne illness</p>
  </footer>
</section>

<!-- Back: Teppanyaki lunch -->
<section class="menu-side menu-side--back">
  <div class="brand-badge brand-badge--back"><span>Kestrelwood</span><span>Restaurnt</span></div>

  <h2 class="section-heading" style="left:39px; top:125px; width:152px;">Teppanyaki Lunch</h2>
  <p class="section-note" style="left:207px; top:125px;"><strong>(Served Daily 11AM - 3PM)</strong><br>Served with Miso Soup or Salad,<br>Choice of Rice &amp; Vegetables</p>
  <div class="item-list" style="left:39px; top:165px; width:225px;">
    <div class="item"><span class="item-name">Hibachi Chicken</span><span class="item-price">$ 18</span></div>
    <div class="item"><span class="item-name">Hibachi Shrimp</span><span class="item-price">$ 19</span></div>
    <div class="item"><span class="item-name">Hibachi New York Steak</span><span class="item-price">$ 20</span></div>
    <div class="item"><span class="item-name">Hibachi Salmon</span><span class="item-price">$ 20</span></div>
    <div class="item"><span class="item-name">Teriyaki Beef</span><span class="item-price">$ 19</span></div>
    <div class="item"><span class="item-name">Hibachi Scallop</span><span class="item-price">$ 20</span></div>
    <div class="item"><span class="item-name">Chicken and Shrimp</span><span class="item-price">$ 21</span></div>
    <div class="item"><span class="item-name">Scallop and Shrimp</span><span class="item-price">$ 22</span></div>
    <div class="item"><span class="item-name">New York Steak and Chicken</span><span class="item-price">$ 22</span></div>
    <div class="item"><span class="item-name">New York Steak and Shrimp</span><span class="item-price">$ 23</span></div>
    <div class="item"><span class="item-name">New York Steak and Scallop</span><span class="item-price">$ 24</span></div>
    <div class="item"><span class="item-name">Filet Mignon</span><span class="item-price">$ 23</span></div>
    <div class="item"><span class="item-name">Filet Mignon and Chicken</span><span class="item-price">$ 25</span></div>
    <div class="item"><span class="item-name">Filet Mignon and Shrimp</span><span class="item-price">$ 26</span></div>
    <div class="item" style="background:transparent;"><span class="item-name"></span><span class="item-price">$ 27</span></div>
  </div>
  <div class="food-photo photo-rice" style="left:281px; top:170px;" role="img" aria-label="Photo of hibachi beef with fried rice"></div>
  <div class="food-photo photo-gold" style="left:281px; top:259px;" role="img" aria-label="Photo of tempura on a white plate"></div>
  <div class="food-photo photo-rice" style="left:281px; top:348px;" role="img" aria-label="Photo of steak with fried rice"></div>

  <h2 class="section-heading" style="left:39px; top:590px; width:113px;">Special Menu</h2>
  <p class="section-note" style="left:207px; top:590px;"><strong>Ages 12 and Under - Ages 65 and older</strong><br>Served with Miso Soup or Salad,<br>Choice of Rice &amp; Vegetables</p>
  <div class="item-list" style="left:39px; top:630px; width:225px;">
    <div class="item"><span class="item-name">Hibachi Chicken</span><span class="item-price">$ 15</span></div>
    <div class="item"><span class="item-name">Hibachi Shrimp</span><span class="item-price">$ 16</span></div>
    <div class="item"><span class="item-name">Hibachi New York Steak</span><span class="item-price">$ 18</span></div>
    <div class="item"><span class="item-name">Hibachi Scallop</span><span class="item-price">$ 18</span></div>
    <div class="item"><span class="item-name">Teriyaki Beef</span><span class="item-price">$ 16</span></div>
  </div>
  <div class="rule-gold"></div>

  <div class="scenery-fade" role="img" aria-label="Faint palm tree and bay scenery"></div>

  <footer class="footer-band footer-band--back">
    <span class="social-label">Finde us on SocialMedia</span>
    <span class="social-dots"><span class="social-dot"></span><span class="social-dot"></span></span>
    <span class="social-handle">@kestrelwoodbay</span>
  </footer>
</section>

</body>
</html>
```